Social house sales

An app that allows someone to search for houses for sale in a certain city or post code...then returns the results and allows the user to like or comment on each property for sale, and @mention others who are users.
UPDATE:
May i know whats your apps name?and please attach the logo.
also - No logo yet! But the name is ''Plimo''
can i get more specific how many pages you want? - Five pages of the mocked up is fine
can you provide the wireframe? - I haven''t done any wire frames, looking for inspiration! Registration/opening splash page, search page, results page, comment/liking, @mentioning someone - those could be five views
and are this app have profile page? No
login with qz or zelbo or pramvek? QZ
which OS i should design it? (IOS,Android) iOS
House buyers, renters
House

```html
<!DOCTYPE html>
<html lang="en">
<head>
<meta charset="utf-8">
<title>Plimo – app screens</title>
<link href="https://fonts.googleapis.com/css2?family=Open+Sans:ital,wght@0,400;0,600;0,700;1,700;1,800&family=Lato:wght@400;700&display=swap" rel="stylesheet">
<style>
:root{
  --green:#93c41d;
  --orange:#f7661f;
  --mustard:#e1ab0b;
  --teal:#3cbfbf;
  --sky:#5cc2e9;
  --slate:#4f5c6b;
  --panel:#f5f5f4;
  --line:#d9d9d9;
  --ink:#333;
  --muted:#8a8a8a;
  --white:#fff;
}
*{box-sizing:border-box;margin:0;padding:0}
html,body{width:1200px;height:1000px;overflow:hidden;background:var(--white)}
body{position:relative;font-family:"Open Sans",Arial,sans-serif;color:var(--ink)}
.abs{position:absolute}
.app-bar{position:absolute;height:45px;background:var(--green);display:flex;align-items:center;justify-content:center;color:var(--white)}
.app-bar .title{font-style:italic;font-weight:800;font-size:24px;letter-spacing:.5px}
.app-bar .back{position:absolute;left:16px;top:10px}
.app-bar .menu{position:absolute;right:18px;top:13px}
.band{position:absolute;display:flex;align-items:center;justify-content:center;color:var(--white);font-size:15px}
.photo{position:absolute;border-radius:2px}
.tab{position:absolute;top:75px;height:25px;font-size:9px;display:flex;align-items:center;justify-content:center;color:#9a9a92;background:#e4e3dc}
.tab.active{background:#f26b3a;color:var(--white)}
.hero-text{position:absolute;color:var(--white)}
.icon-bar{position:absolute;left:28px;top:410px;width:358px;height:56px;background:var(--mustard);display:flex}
.icon-bar span{flex:1;display:flex;align-items:center;justify-content:center;border-right:1px solid rgba(255,255,255,.25)}
.icon-bar span:last-child{border-right:none}
.stats{position:absolute;display:flex;align-items:center;gap:4px;font-size:14px;color:#444}
.stats b{font-weight:400;font-size:17px}
.comment-area{position:absolute;left:30px;top:572px;width:354px;height:410px;background:var(--panel)}
.comment-input{position:absolute;left:37px;top:581px;width:261px;height:98px;background:var(--white);border:1px solid #aaa;font-size:14px;color:#bbb;padding:10px}
.send{position:absolute;left:311px;top:652px;width:58px;height:28px;background:var(--mustard);color:var(--white);font-size:15px;display:flex;align-items:center;justify-content:center}
.bubble{position:absolute;background:linear-gradient(#fff,#f0f0f0);border:1px solid #c9c9c9;border-radius:3px;padding:9px 11px;font-family:Arial,sans-serif;box-shadow:0 1px 2px rgba(0,0,0,.12)}
.bubble h4{font-size:9px;font-weight:400;color:#222;margin-bottom:3px}
.bubble p{font-size:9px;line-height:13px;color:#444}
.bubble .meta{font-size:8px;color:#888;margin-top:8px}
.bubble:after{content:"";position:absolute;right:-6px;top:10px;width:10px;height:10px;background:#fff;border-top:1px solid #c9c9c9;border-right:1px solid #c9c9c9;transform:rotate(45deg)}
.avatar{position:absolute;background:linear-gradient(135deg,#c98a6a,#7a4a3a);box-shadow:0 1px 2px rgba(0,0,0,.3)}
.scroll{position:absolute;width:5px;background:#c4c4c4;border-radius:3px}
.listing{position:absolute;left:413px;width:359px;height:118px;background:var(--white);border-bottom:1px solid #eee}
.listing .addr{position:absolute;left:160px;top:40px;font-family:Lato,sans-serif;font-weight:700;font-size:12px;color:#444}
.listing .city{position:absolute;left:160px;top:55px;font-family:Lato,sans-serif;font-style:italic;font-size:11px;color:#aaa}
.listing .social{position:absolute;left:166px;top:78px;display:flex;align-items:center;gap:4px;font-size:17px;color:#444}
.profile{position:absolute;left:413px;top:558px;width:354px;height:177px;background:var(--panel)}
.field{position:absolute;left:413px;width:354px;font-size:17px}
.field .k{position:absolute;right:204px;font-size:13px;color:var(--muted)}
.field .v{position:absolute;left:172px;color:#333}
.more{position:absolute;left:413px;top:921px;width:354px;height:50px;background:#f3f3f1;font-size:12px;color:#999;display:flex;align-items:center;justify-content:center}
.popup{position:absolute;left:816px;top:157px;width:324px;height:108px;background:linear-gradient(#fff,#e6e6e6);border:1px solid #aaa;border-radius:4px;box-shadow:0 2px 6px rgba(0,0,0,.3)}
.popup h3{position:absolute;left:107px;top:20px;font-size:12px;font-weight:700;color:#111;font-family:Arial,sans-serif}
.popup p{position:absolute;left:107px;top:37px;width:200px;font-size:10px;line-height:14px;color:#222;font-family:Arial,sans-serif}
.input{position:absolute;left:826px;width:304px;height:45px;border:1px solid #aaa;background:var(--white);display:flex;align-items:center;padding-left:22px;font-size:13px;color:#ccc}
.submit{position:absolute;left:826px;top:813px;width:304px;height:45px;background:var(--sky);color:var(--white);font-weight:700;font-size:13px;letter-spacing:1.5px;display:flex;align-items:center;justify-content:center}
.forgot{position:absolute;left:826px;top:874px;width:304px;text-align:center;font-size:10px;color:#8a8a8a;text-decoration:underline}
.alt-login{position:absolute;left:797px;top:919px;width:361px;height:52px;background:var(--slate);color:var(--white);font-size:11px;display:flex;align-items:center;justify-content:center}
.alt-login b{font-weight:700;margin-left:4px}
</style>
</head>
<body>

<!-- Shared icon definitions -->
<svg width="0" height="0" style="position:absolute">
  <defs>
    <symbol id="i-back" viewBox="0 0 34 24"><path d="M13 2 L2 11 L13 20 L13 14 C21 13 27 15 32 21 C30 11 23 7 13 7 Z" fill="#fff"/></symbol>
    <symbol id="i-menu" viewBox="0 0 24 18"><g fill="#fff"><rect x="0" y="0" width="4" height="4"/><rect x="0" y="7" width="4" height="4"/><rect x="0" y="14" width="4" height="4"/><rect x="7" y="1" width="17" height="2"/><rect x="7" y="8" width="17" height="2"/><rect x="7" y="15" width="17" height="2"/></g></symbol>
    <symbol id="i-heart" viewBox="0 0 24 22"><path d="M12 20 C5 14 2 11 2 7 C2 4 4 2 7 2 C9 2 11 3 12 5 C13 3 15 2 17 2 C20 2 22 4 22 7 C22 11 19 14 12 20 Z" fill="none" stroke="currentColor" stroke-width="1.6"/></symbol>
    <symbol id="i-chat" viewBox="0 0 24 22"><path d="M12 3 C6 3 2 6 2 10 C2 13 4 15 7 16 L6 20 L11 17 C11 17 12 17 12 17 C18 17 22 14 22 10 C22 6 18 3 12 3 Z" fill="none" stroke="currentColor" stroke-width="1.6"/></symbol>
    <symbol id="i-share" viewBox="0 0 24 22"><g fill="none" stroke="currentColor" stroke-width="1.6"><circle cx="18" cy="4" r="3"/><circle cx="5" cy="11" r="3"/><circle cx="18" cy="18" r="3"/><path d="M8 9.5 L15 5.5 M8 12.5 L15 16.5"/></g></symbol>
    <symbol id="i-pin" viewBox="0 0 40 60"><path d="M20 58 C14 44 2 34 2 20 C2 10 10 2 20 2 C30 2 38 10 38 20 C38 34 26 44 20 58 Z" fill="currentColor" stroke="rgba(0,0,0,.25)" stroke-width="1.5"/><circle cx="20" cy="19" r="9" fill="none" stroke="#fff" stroke-width="3"/></symbol>
  </defs>
</svg>

<!-- ============ Screen 1 : property detail ============ -->
<header class="app-bar" style="left:30px;top:23px;width:359px">
  <svg class="back" width="34" height="24"><use href="#i-back"/></svg>
  <span class="title">PLIMO</span>
  <svg class="menu" width="24" height="18"><use href="#i-menu"/></svg>
</header>

<div class="tab active" style="left:31px;width:54px">Photos</div>
<div class="tab" style="left:93px;width:70px">Street View</div>
<div class="tab" style="left:172px;width:46px">Map</div>

<div class="photo" role="img" aria-label="Photo of an open-plan living and dining room with glass walls looking over water and mountains" style="left:30px;top:105px;width:352px;height:242px;border-radius:0;background:linear-gradient(180deg,#b9c4cf 0%,#8e99a2 40%,#5a4c44 70%,#2c2420 100%)"></div>
<svg class="abs" style="left:349px;top:116px" width="20" height="20"><circle cx="10" cy="10" r="7.5" fill="none" stroke="#fff" stroke-width="1.5"/><path d="M6 10 H13 M10 7 L13 10 L10 13" fill="none" stroke="#fff" stroke-width="1.5"/></svg>
<div class="hero-text" style="left:49px;top:287px;font-weight:700;font-size:21px">Street Name</div>
<div class="hero-text" style="left:49px;top:312px;font-weight:700;font-size:13px">Full address</div>
<div class="hero-text" style="left:193px;top:293px;width:36px;height:36px;border-radius:50%;background:#f26b3a;font-size:9px;display:flex;align-items:center;justify-content:center">RENT</div>
<div class="hero-text" style="left:249px;top:286px;font-weight:700;font-size:25px">$600 / Wk</div>
<div class="hero-text" style="left:249px;top:319px;font-style:italic;font-size:12px">Bond: $2,400</div>

<div class="photo" role="img" aria-label="Thumbnail: living room" style="left:34px;top:357px;width:54px;height:46px;background:linear-gradient(135deg,#b08a5a,#5d4330)"></div>
<div class="photo" role="img" aria-label="Thumbnail: bedroom" style="left:93px;top:357px;width:54px;height:46px;background:linear-gradient(135deg,#d8d2c8,#8f8478)"></div>
<div class="photo" role="img" aria-label="Thumbnail: kitchen" style="left:152px;top:357px;width:54px;height:46px;background:linear-gradient(135deg,#c9c2b5,#6f6a62)"></div>
<div class="photo" role="img" aria-label="Thumbnail: lounge" style="left:211px;top:357px;width:54px;height:46px;background:linear-gradient(135deg,#e8d6bd,#b08a66)"></div>
<div class="photo" role="img" aria-label="Thumbnail: dining area" style="left:270px;top:357px;width:54px;height:46px;background:linear-gradient(135deg,#e3ddd4,#a89b8b)"></div>
<div class="photo" role="img" aria-label="Thumbnail: pool terrace" style="left:328px;top:357px;width:54px;height:46px;background:linear-gradient(135deg,#cfe0ea,#7aa5bf)"></div>

<nav class="icon-bar" style="color:#fff">
  <span><svg width="20" height="18"><use href="#i-heart"/></svg></span>
  <span><svg width="20" height="18"><use href="#i-chat"/></svg></span>
  <span><svg width="20" height="18"><use href="#i-share"/></svg></span>
  <span><svg width="20" height="18" viewBox="0 0 20 18"><path d="M1 3 L7 1 L13 3 L19 1 V15 L13 17 L7 15 L1 17 Z M7 1 V15 M13 3 V17" fill="none" stroke="#fff" stroke-width="1.5"/></svg></span>
  <span><svg width="20" height="18" viewBox="0 0 20 18"><rect x="1" y="1" width="18" height="16" rx="2" fill="none" stroke="#fff" stroke-width="1.5"/><path d="M6 13 V8 M10 13 V5 M14 13 V9" stroke="#fff" stroke-width="1.5"/></svg></span>
  <span><svg width="20" height="20" viewBox="0 0 20 20"><circle cx="10" cy="10" r="3" fill="none" stroke="#fff" stroke-width="1.5"/><path d="M10 1 V4 M10 16 V19 M1 10 H4 M16 10 H19 M3.6 3.6 L5.8 5.8 M14.2 14.2 L16.4 16.4 M3.6 16.4 L5.8 14.2 M14.2 5.8 L16.4 3.6" stroke="#fff" stroke-width="1.8"/><circle cx="10" cy="10" r="6" fill="none" stroke="#fff" stroke-width="1.5"/></svg></span>
  <span><svg width="16" height="22" viewBox="0 0 16 22"><path d="M8 21 C5 15 1 12 1 7.5 C1 3.5 4 1 8 1 C12 1 15 3.5 15 7.5 C15 12 11 15 8 21 Z" fill="none" stroke="#fff" stroke-width="1.5"/><circle cx="8" cy="7.5" r="2.5" fill="none" stroke="#fff" stroke-width="1.5"/></svg></span>
</nav>

<div class="stats" style="left:40px;top:480px"><svg width="22" height="20"><use href="#i-heart"/></svg><b>10</b> likes</div>
<div class="stats" style="left:148px;top:480px"><svg width="22" height="20"><use href="#i-chat"/></svg><b>2</b> comments</div>
<div class="stats" style="left:289px;top:480px"><svg width="22" height="20"><use href="#i-share"/></svg><b>1</b> share</div>

<div class="band" style="left:30px;top:517px;width:359px;height:44px;background:var(--orange)">Comment</div>

<section class="comment-area"></section>
<div class="comment-input">Comment</div>
<div class="avatar" role="img" aria-label="Current user avatar" style="left:313px;top:582px;width:54px;height:54px"></div>
<div class="send">Send</div>

<article class="bubble" style="left:36px;top:697px;width:261px;height:79px">
  <h4>NAME NAME</h4>
  <p>it amet, consectetur adipi cing elit. Donec risus risus, feugiat sit amet egestas quis, pharetra non metus.</p>
  <div class="meta">1 Comment.&nbsp; 2 Like</div>
</article>
<div class="avatar" role="img" aria-label="Commenter avatar" style="left:311px;top:697px;width:55px;height:55px"></div>

<article class="bubble" style="left:75px;top:787px;width:219px;height:90px">
  <h4>My Name</h4>
  <p>it amet, consectetur adipi cing elit. Donec risus risus, feugiat sit amet egestas quis, pharetra non metus.</p>
  <div class="meta" style="margin-top:6px"><span style="color:#444">Comment .</span>&nbsp; Like&nbsp; Edit</div>
</article>
<div class="avatar" role="img" aria-label="Own avatar" style="left:310px;top:787px;width:54px;height:54px"></div>

<article class="bubble" style="left:36px;top:891px;width:261px;height:78px">
  <h4>NAME NAME</h4>
  <p>it amet, consectetur adipi cing elit. Donec risus risus, feugiat sit amet egestas quis, pharetra non metus.</p>
  <div class="meta">1 Comment.&nbsp; 2 Like</div>
</article>
<div class="avatar" role="img" aria-label="Commenter avatar" style="left:311px;top:891px;width:55px;height:55px"></div>
<div class="scroll" style="left:373px;top:697px;height:123px"></div>

<!-- ============ Screen 2 : similar listings & agent ============ -->
<header class="app-bar" style="left:413px;top:23px;width:359px">
  <svg class="back" width="34" height="24"><use href="#i-back"/></svg>
  <span class="title">PLIMO</span>
  <svg class="menu" width="24" height="18"><use href="#i-menu"/></svg>
</header>

<div class="band" style="left:413px;top:82px;width:359px;height:45px;background:var(--teal)">Similar properties for Rent</div>

<div class="listing" style="top:130px">
  <div class="photo" role="img" aria-label="Apartment with red sofa" style="left:30px;top:26px;width:112px;height:86px;background:linear-gradient(135deg,#d9d4cc,#b0473f)"></div>
  <div class="addr">Lv 33/2 Merrow Street</div><div class="city">Halden NSW 2000</div>
  <div class="social"><svg width="22" height="20"><use href="#i-heart"/></svg>10 <svg width="22" height="20"><use href="#i-chat"/></svg>2 <svg width="22" height="20"><use href="#i-share"/></svg>1</div>
</div>
<div class="listing" style="top:254px;background:#fafafa">
  <div class="photo" role="img" aria-label="Bright living room with dark sofa" style="left:30px;top:26px;width:112px;height:88px;background:linear-gradient(135deg,#e4e1dc,#6b6660)"></div>
  <div class="addr">Lv 33/2 Merrow Street</div><div class="city">Halden NSW 2000</div>
  <div class="social" style="top:84px"><svg width="22" height="20"><use href="#i-heart"/></svg>10 <svg width="22" height="20"><use href="#i-chat"/></svg>2 <svg width="22" height="20"><use href="#i-share"/></svg>1</div>
</div>
<div class="listing" style="top:376px">
  <div class="photo" role="img" aria-label="Bedroom with wooden bed" style="left:30px;top:26px;width:112px;height:86px;background:linear-gradient(135deg,#e0ddd8,#9a6a3e)"></div>
  <div class="addr">Lv 33/2 Merrow Street</div><div class="city">Halden NSW 2000</div>
  <div class="social" style="top:88px"><svg width="22" height="20"><use href="#i-heart"/></svg>10 <svg width="22" height="20"><use href="#i-chat"/></svg>2 <svg width="22" height="20"><use href="#i-share"/></svg>1</div>
</div>
<div class="scroll" style="left:760px;top:137px;height:125px;width:4px"></div>

<div class="band" style="left:415px;top:506px;width:359px;height:44px;background:var(--mustard)">NAME NAME</div>

<section class="profile">
  <div class="avatar" role="img" aria-label="Agent profile photo" style="left:30px;top:30px;width:120px;height:120px;border-radius:50%;box-shadow:none"></div>
  <div class="abs" style="left:172px;top:49px;font-size:13px;color:#444">Name Surname <span style="font-size:11px">(582 <svg width="14" height="14" viewBox="0 0 20 20" style="vertical-align:-2px"><path d="M10 1 L12.6 7 L19 7.4 L14 11.6 L15.6 18 L10 14.5 L4.4 18 L6 11.6 L1 7.4 L7.4 7 Z" fill="#f4c21a" stroke="#d49a00"/></svg>)</span></div>
  <div class="abs" style="left:172px;top:69px;font-size:11px;color:#888">from <span style="text-decoration:underline">Tallis &amp; Brook</span></div>
</section>

<div class="field" style="top:766px"><span class="k">Age</span><span class="v">27</span></div>
<div class="field" style="top:819px"><span class="k" style="top:2px">Gender</span><span class="v">Female</span></div>
<div class="field" style="top:871px"><span class="k" style="top:2px">Comments</span><span class="v">236</span></div>

<div class="more">More</div>

<!-- ============ Screen 3 : map & login ============ -->
<header class="app-bar" style="left:796px;top:16px;width:358px">
  <svg class="back" width="34" height="24" style="top:9px"><use href="#i-back"/></svg>
  <span class="title">PLIMO</span>
  <svg class="menu" width="24" height="18" style="top:13px"><use href="#i-menu"/></svg>
</header>

<div class="photo" role="img" aria-label="Road map of the search region" style="left:796px;top:66px;width:357px;height:516px;border-radius:0;background:linear-gradient(160deg,#f1eee6 0%,#e8e6dc 45%,#dfe6cf 70%,#ecebe3 100%)"></div>

<div class="abs" style="left:818px;top:292px;width:24px;height:200px;border-radius:12px;background:#fff;border:1px solid #999"></div>
<div class="abs" style="left:823px;top:312px;width:14px;height:160px;border-radius:7px;background:linear-gradient(#777 0%,#777 28%,#f5a800 28%);"></div>
<div class="abs" style="left:815px;top:350px;width:30px;height:20px;border:1px solid #999;border-radius:3px;background:#fff"><svg width="30" height="20" viewBox="0 0 30 20"><path d="M8 6 H22 M8 10 H22 M8 14 H22" stroke="#e2a000" stroke-width="2"/></svg></div>
<div class="abs" style="left:824px;top:292px;font-size:15px;font-weight:700;color:#333">+</div>
<div class="abs" style="left:825px;top:472px;font-size:15px;font-weight:700;color:#333">−</div>

<svg class="abs" style="left:895px;top:278px;color:#8dc21e" width="58" height="80"><use href="#i-pin"/></svg>
<svg class="abs" style="left:1024px;top:345px;color:#2a8fdb" width="44" height="62"><use href="#i-pin"/></svg>
<svg class="abs" style="left:867px;top:467px;color:#2a8fdb" width="44" height="62"><use href="#i-pin"/></svg>
<svg class="abs" style="left:1041px;top:496px;color:#2a8fdb" width="44" height="62"><use href="#i-pin"/></svg>

<div class="popup">
  <div class="photo" role="img" aria-label="Listing thumbnail: dining room" style="left:20px;top:17px;width:68px;height:68px;border:3px solid #fff;box-shadow:0 0 0 1px #bbb;background:linear-gradient(135deg,#d8cfc0,#4d4038)"></div>
  <h3>Lorem ipsum dolor</h3>
  <p>sit amet, consectetur adipi cing elit. Donec risus risus, feugiat sit amet eges-tas quis, pharetra non metus.</p>
  <svg class="abs" style="left:300px;top:4px" width="20" height="20"><path d="M4 4 L16 16 M16 4 L4 16" stroke="#111" stroke-width="3"/></svg>
</div>
<svg class="abs" style="left:914px;top:264px" width="20" height="12"><path d="M0 0 L10 11 L20 0 Z" fill="#e6e6e6"/><path d="M0 0 L10 11 L20 0" fill="none" stroke="#aaa"/></svg>

<div class="band" style="left:797px;top:609px;width:360px;height:44px;background:var(--orange)">Login Form</div>

<div class="input" style="top:684px"><svg width="16" height="16" viewBox="0 0 16 16"><circle cx="8" cy="5" r="3.5" fill="none" stroke="#aaa"/><path d="M1.5 15 C2 10 14 10 14.5 15 Z" fill="none" stroke="#aaa"/></svg><span style="width:1px;height:18px;background:#333;margin-left:17px"></span></div>
<div class="input" style="top:749px"><svg width="14" height="16" viewBox="0 0 14 16"><rect x="1.5" y="7" width="11" height="8" fill="none" stroke="#ccc"/><path d="M4 7 V4.5 C4 1.5 10 1.5 10 4.5 V7" fill="none" stroke="#ccc"/></svg><span style="margin-left:22px">Password</span></div>
<div class="submit">SUBMIT</div>
<div class="forgot">Forgot your password?</div>
<div class="alt-login">Login with <b>Vantro</b></div>

</body>
</html>
```